Horizontal scrolling homepage | ||
Consulting company needing a unique layout | ||
Consulting | ||
Qorvinex does consulting and implementation projects within CRM which are the processes around sales, marketing, service, call centers, web shops and more. Even though such engagements of course need the technical involvement from IT, it for sure also needs the business and in this segment the business consists of extrovert colorful people. |
The homepage must be different than the competitors and one way of doing that is by having horizontal scrolling with a menu bar on the left (if the design would be better, you can place it on the top). If it can be done in a cool way, then the left menu bar could be a bit to the right of the left border so that the scrolling background is visible. The scrolling should accelerate and de-accelerate when moving to the part of the homepage that should be displayed. There should not be a scrollbar. Menu: Start (or logo) Packages Services Next Step Career About On the start page there should be a combined sign up for newsletter and contact form (like here: brimtala[dot]dk[slash]om-brimtala). (Title, first name, last name, e-mail, mobile phone number, checkbox for Newsletter sign up and a free text field). The homepage must be easy to extend with additional texts. There should be teasers on the start page that will navigate the user to a place on one of the subpages with more information. It could be interesting to have flipping boxes like in Window Mobile, where one side of the box has a teaser one-liner and when the mouse hovers over it flips and the solution is on the back and when clicked, the page scrolls to the place with more information. But I do not know how easy that will be to implement with HTML5. Inspire me. In addition add the content that normally is part of a start page. You will find logo and teasers as attachments. For additional text use dummy latin. |
Cutting-Edge Unique/Creative Flashy Professional Corporate Modern Elegant Service Oriented |
See logo | ||
Arial Verdana Trebuchet MS |
left side | ||
http://www.morvenquaily.co.uk/ | ||
http://www.pravessa.com/ | ||
http://tunbelfield.com/ | ||
The homepage should be compatible with Internet Explorer and Crome, it should be accessible from Android pads and phones and Apple Iphones and Ipads, but I assume that will all automatically be possible when HTML5 is used for the development. The homepage must be easy to extend with additional menu items / texts. |

```html
<!DOCTYPE html>
<html lang="en">
<head>
<meta charset="utf-8">
<title>Qorvinex – CRM consulting</title>
<link href="https://fonts.googleapis.com/css2?family=Open+Sans:wght@400;600;700&display=swap" rel="stylesheet">
<style>
  :root {
    --page-bg: #e4e6e7;
    --page-line: #d9dcdd;
    --panel: #ffffff;
    --sidebar: #f3f4f4;
    --strip: #5b5f62;
    --strip-light: #eceeee;
    --ink: #3d4245;
    --ink-soft: #6d7275;
    --green: #56a830;
    --green-dark: #3f8f1f;
    --navy: #1f3a68;
    --red: #c8282c;
    --chart-a: #dfe7ee;
    --chart-b: #9fb7cc;
  }
  * { box-sizing: border-box; margin: 0; padding: 0; }
  html, body { width: 1200px; height: 526px; overflow: hidden; }
  body {
    font-family: "Open Sans", Arial, sans-serif;
    color: var(--ink);
    background:
      repeating-linear-gradient(90deg, transparent 0 58px, var(--page-line) 58px 60px),
      var(--page-bg);
    position: relative;
  }

  /* Sidebar */
  .sidebar {
    position: absolute; left: 108px; top: 0; width: 176px; height: 478px;
    background: var(--sidebar);
    border-radius: 0 0 10px 10px;
    box-shadow: 0 2px 8px rgba(0,0,0,.18);
  }
  .brand {
    margin: 14px 12px 0; height: 90px; border-radius: 8px;
    background: #fff; border: 1px solid #d6d9da;
    display: flex; align-items: center; justify-content: center; gap: 8px;
  }
  .brand-mark { width: 22px; height: 22px; border-radius: 50%; background: var(--green); }
  .brand-name { font-size: 22px; font-weight: 700; color: var(--navy); }
  .menu { list-style: none; margin: 30px 0 0 22px; }
  .menu li { display: flex; align-items: flex-start; gap: 10px; height: 58px; }
  .menu svg { margin-top: 4px; flex: none; }
  .menu-title { font-size: 15px; font-weight: 700; color: var(--navy); line-height: 1.1; display: block; }
  .menu-sub { font-size: 10px; color: var(--ink-soft); display: block; }
  .follow { position: absolute; left: 0; right: 0; top: 418px; text-align: center; }
  .follow-label { font-size: 10px; color: var(--green-dark); font-weight: 600; display: block; }
  .follow-name { font-size: 14px; font-weight: 700; color: var(--navy); }

  /* Vertical tabs */
  .tab {
    position: absolute; top: 60px; height: 432px; width: 34px;
    writing-mode: vertical-rl;
    font-size: 10px; font-weight: 700; letter-spacing: .5px;
    display: flex; align-items: center; justify-content: flex-start;
    padding-top: 14px; text-transform: uppercase;
  }
  .tab-dark { background: var(--strip); color: #fff; }
  .tab-light { background: var(--strip-light); color: var(--ink); border-left: 1px solid #cfd2d3; }

  /* Main slide */
  .slide {
    position: absolute; left: 324px; top: 60px; width: 564px; height: 432px;
    background: var(--panel); overflow: hidden;
    box-shadow: 0 1px 4px rgba(0,0,0,.15);
  }
  .slide .tab { top: 0; left: 0; height: 100%; }
  .slide-visual {
    position: absolute; right: 0; top: 0; width: 300px; height: 100%;
    background: linear-gradient(200deg, var(--chart-b) 0%, var(--chart-a) 45%, #ffffff 100%);
  }
  .slide-copy { position: absolute; left: 56px; top: 34px; width: 330px; }
  .slide-title { font-size: 25px; font-weight: 400; line-height: 1.15; }
  .slide-title .sub { font-size: 16px; font-weight: 600; display: block; margin-top: 2px; }
  .slide-title mark { background: var(--green); color: #fff; padding: 0 3px; }
  .slide-copy p { font-size: 11.5px; line-height: 1.5; margin-top: 8px; color: var(--ink); }
  .read-more {
    margin-top: 52px; display: inline-flex; align-items: center; gap: 8px;
    background: var(--navy); color: #fff; font-size: 11px; font-weight: 700;
    padding: 7px 18px 7px 10px; border-radius: 3px; text-decoration: none;
  }

  /* Sales enquiry */
  .sales { position: absolute; left: 893px; top: 18px; display: flex; gap: 8px; align-items: center; }
  .sales-label { font-size: 12px; color: var(--green-dark); display: block; }
  .sales-number { font-size: 17px; font-weight: 600; color: var(--ink); }

  /* Contact tab */
  .contact-tab {
    position: absolute; right: 0; top: 132px; width: 30px; height: 134px;
    background: var(--green); color: #fff; writing-mode: vertical-rl;
    font-size: 11px; font-weight: 700; display: flex; align-items: center; justify-content: center;
    border-radius: 4px 0 0 4px;
  }
</style>
</head>
<body>

<nav class="sidebar">
  <div class="brand"><span class="brand-mark"></span><span class="brand-name">Qorvinex</span></div>
  <ul class="menu">
    <li><svg width="20" height="16" viewBox="0 0 20 16"><path d="M2 8l5 5L18 2" fill="none" stroke="#56a830" stroke-width="3"/></svg><div><span class="menu-title">PACKAGES</span><span class="menu-sub">what we offers</span></div></li>
    <li><svg width="20" height="16" viewBox="0 0 20 16"><path d="M2 8l5 5L18 2" fill="none" stroke="#56a830" stroke-width="3"/></svg><div><span class="menu-title">SERVICES</span><span class="menu-sub">what we offers</span></div></li>
    <li><svg width="20" height="16" viewBox="0 0 20 16"><path d="M2 8l5 5L18 2" fill="none" stroke="#56a830" stroke-width="3"/></svg><div><span class="menu-title">NEXT STEP</span><span class="menu-sub">what we have ahead</span></div></li>
    <li><svg width="20" height="16" viewBox="0 0 20 16"><path d="M2 8l5 5L18 2" fill="none" stroke="#56a830" stroke-width="3"/></svg><div><span class="menu-title">CAREERS</span><span class="menu-sub">Return with us</span></div></li>
    <li><svg width="20" height="16" viewBox="0 0 20 16"><path d="M2 8l5 5L18 2" fill="none" stroke="#56a830" stroke-width="3"/></svg><div><span class="menu-title">ABOUT US</span><span class="menu-sub">who we are</span></div></li>
  </ul>
  <div class="follow"><span class="follow-label">Follow us on</span><span class="follow-name">Netlinka</span></div>
</nav>

<div class="tab tab-dark" style="left:288px">Vantrel projects are big and costly. Right?</div>

<section class="slide">
  <div class="tab tab-dark" style="background:#6a6e71">Looking for a system to control your marketing...</div>
  <div class="slide-visual" role="img" aria-label="Business charts and printed reports on a desk"></div>
  <div class="slide-copy">
    <h1 class="slide-title">Looking for a system to
      <span class="sub">control your <mark>marketing, sale or service processes?</mark></span></h1>
    <p>Then Vantrel's combined setup of software to a reduced price, and delivery, called Rapid Deployment Service, is your solution.</p>
    <p>Qorvinex has already delivered this concept in the Nordic; contact us for a discussion of how you can gain and grow from this.</p>
    <a class="read-more" href="#"><svg width="14" height="14" viewBox="0 0 14 14"><circle cx="7" cy="7" r="6.5" fill="#fff"/><path d="M5 4l3 3-3 3" fill="none" stroke="#1f3a68" stroke-width="1.8"/></svg>READ MORE</a>
  </div>
</section>

<div class="tab tab-light" style="left:893px">Need something special for your Vantrel implementation?</div>
<div class="tab tab-light" style="left:927px">How can we help you? Really?</div>
<div class="tab tab-light" style="left:961px">Collaboration</div>

<div class="sales">
  <svg width="24" height="24" viewBox="0 0 24 24"><path d="M5 3l4 0 2 5-3 2c1 3 3 5 6 6l2-3 5 2v4c0 1-1 2-2 2C10 21 3 14 3 5c0-1 1-2 2-2z" fill="#c8282c"/></svg>
  <div><span class="sales-label">For sales enquiry</span><span class="sales-number">+45 3174 2058</span></div>
</div>

<div class="contact-tab">CONTACT US</div>

</body>
</html>
```